We need a modern WIX website for Brightwave Surface Renewal Australia (Laser/Industrial/Engineering)

We need a website for Wix (coded) for our laser restoration and industrial cleaning business.

It will need to be 4-6 pages.
Pages may include:
Home
About
Why Laser
Capabilities
There needs to be a contact / quote form

We do not want boring institutional design, so please do try to be a little creative (but not artsy, more engineering / laser etc). We hesitate with boxy wordpress looking templates, so please bring in strip backgrounds and sliders etc;

Our brand colours are blue and red, but a sharp modern site relative to the industry and work is important.

We envision the home page to take visitors on a informed journey of who, what, why, how, explaining the capability of laser science across contaminants, industries and surfaces.

We envision the home page to be strips:
- landing
- intro

-Why choose laser / What is laser cleaning
Minimum downtime, no surface damage, no environmental impact, no mess, no waste, complete restoration (we have an explainer video)

- Contaminants
Bacteria, Rust, Corrosion, Oxides, Grease, Oil, Paint, Stains, Mold, Soot / Carbon, Graffiti, Coatings, Dirt, Residue

- Surfaces
Metals, Engines/Parts/Components, Tools, Machinery, Bricks/Blockwork, Concrete, Paint, Stone, Wood, Aluminium

- Industries
Medical/Sterile, Hospitality, Bio Hazardous, Construction, Infrastructure, Property, Industrial, Engineer, Automotive, Marine, Heritage, Non Destructive Testing,

----
Here is some info on the company below:

"Background Information - Brightwave Surface Renewal Australia (BSRA) is a leading provider of advanced laser restoration services for the residential, commercial, medical, hazardous and industrial sectors, offering waste free, chemical free and damage free complete restoration of metals, concrete, wood, stone and heritage, hygiene and hazard surfaces, with complete removal of coatings, bacteria, paint, rust, graffiti, mold and fire ash (soot), and preparation and treating for welding and bonding.
Servicing Melbourne and Victoria, with additional services available Australia wide, BSRA offers a 24/7 call-out service to your site.
With no downtime to your operations, we offer a timely resolution to your cleaning and maintenance needs."

We have attached some inspiration of websites we like the flow/feel of, but feel free to put your best designs forward.

You are welcome to use dummy headers and text at this stage, as design and feel is most important, and we can add text later.

```html
<!DOCTYPE html>
<html lang="en">
<head>
<meta charset="utf-8">
<title>BSRA – Brightwave Surface Renewal Australia</title>
<link href="https://fonts.googleapis.com/css2?family=Michroma&family=Fira+Sans:wght@400;500&family=Fira+Sans+Condensed:wght@400&display=swap" rel="stylesheet">
<style>
  :root{
    --red:#e8141c;
    --blue:#1a73c0;
    --black:#000;
    --charcoal:#282828;
    --light:#ececec;
    --white:#fff;
    --ghost:#4a4a4a;
    --text:#1d1d1d;
  }
  *{margin:0;padding:0;box-sizing:border-box}
  html,body{width:1200px;height:3124px;overflow:hidden}
  body{position:relative;background:var(--black);font-family:"Fira Sans",sans-serif;color:var(--white)}
  .display{font-family:"Michroma",sans-serif;text-transform:uppercase}
  .abs{position:absolute}
  .btn{position:absolute;display:flex;align-items:center;justify-content:center;font-family:"Michroma",sans-serif;font-size:14px;color:var(--white);text-transform:uppercase}
  .btn-blue{background:var(--blue)}
  .btn-red{background:var(--red)}
  .btn-outline{border:2px solid var(--red)}

  /* header */
  .site-header{position:absolute;left:0;top:0;width:1200px;height:113px;background:var(--black)}
  .brand{position:absolute;left:113px;top:30px;font-family:"Michroma",sans-serif;font-size:44px;color:var(--white);letter-spacing:2px}
  .nav{position:absolute;top:46px;display:flex;font-family:"Fira Sans Condensed",sans-serif;font-size:15px;left:465px;gap:43px}
  .btn-contact{left:926px;top:28px;width:124px;height:53px;font-size:14px}

  /* hero */
  .hero{position:absolute;left:0;top:113px;width:1200px;height:593px;
    background:linear-gradient(90deg,#a5141c 0%,#8c1620 30%,#3a1a20 55%,#1c2e36 75%,#10161c 100%)}
  .hero-welcome{left:113px;top:132px;font-size:44px}
  .hero-name{left:108px;top:192px;font-size:108px;line-height:1.1}
  .hero-sub{left:113px;top:331px;font-family:"Fira Sans Condensed",sans-serif;font-size:31px}
  .btn-start{left:114px;top:404px;width:152px;height:52px}

  /* why laser */
  .why{position:absolute;left:0;top:706px;width:1200px;height:160px;background:var(--light);color:var(--text)}
  .why-title{position:absolute;width:100%;top:30px;text-align:center;font-size:30px}
  .why-item{position:absolute;top:98px;font-size:17px;font-weight:500}
  .why-active{position:absolute;left:252px;top:77px;width:161px;height:63px;background:linear-gradient(135deg,#c8141b,#ff3a3f 50%,#b51218);color:var(--white);text-align:center;font-size:17px;font-weight:500;padding-top:8px}

  /* about */
  .about{position:absolute;left:0;top:866px;width:1200px;height:605px;background:var(--black)}
  .frame-red{left:113px;top:112px;width:386px;height:342px;border:5px solid var(--red)}
  .frame-white{left:176px;top:175px;width:386px;height:342px;border:5px solid var(--white)}
  .about-photo{left:136px;top:137px;width:387px;height:344px;background:radial-gradient(circle at 50% 85%,#ffce6a 0%,#d2661c 22%,#6a2a14 55%,#1c0e08 100%)}
  .ghost-about{font-size:82px;color:var(--ghost);transform:rotate(-90deg);transform-origin:center;width:420px;text-align:center;left:-124px;top:270px}
  .about-label{left:615px;top:100px;color:var(--red);font-size:15px}
  .about-heading{left:615px;top:140px;width:560px;font-size:28px;line-height:1.6;white-space:nowrap}
  .red{color:var(--red)}
  .about-text{left:615px;top:268px;width:470px;font-family:"Fira Sans Condensed",sans-serif;font-size:14px;line-height:24.8px}
  .btn-learn{left:615px;top:477px;width:146px;height:51px}

  /* contaminants */
  .contaminants{position:absolute;left:0;top:1471px;width:1200px;height:564px;background:var(--charcoal)}
  .cont-title{position:absolute;width:100%;top:55px;text-align:center;font-size:34px}
  .cards{position:absolute;left:113px;top:133px;display:grid;grid-template-columns:repeat(4,235px);grid-auto-rows:145px;column-gap:12px;row-gap:14px}
  .card{background:var(--white);display:flex;align-items:center;padding-left:18px;color:var(--text);font-size:21px;font-weight:500;letter-spacing:.5px}
  .card-icon{width:85px;height:85px;border-radius:50%;background:var(--red);margin-right:18px;display:flex;align-items:center;justify-content:center}
  .btn-viewall-cont{left:527px;top:463px;width:146px;height:51px}
  .ghost-cont{font-size:46px;color:var(--ghost);transform:rotate(-90deg);width:460px;text-align:center;left:910px;top:220px}

  /* surfaces */
  .surfaces{position:absolute;left:0;top:2035px;width:1200px;height:704px;background:var(--black)}
  .tab-surfaces{left:433px;top:86px;width:147px;height:51px}
  .tab-industries{left:612px;top:86px;width:154px;height:51px}
  .surf-heading{left:113px;top:190px;font-size:42px}
  .btn-viewall-surf{left:940px;top:188px;width:147px;height:51px}
  .tile{position:absolute;top:272px;width:280px;height:304px}
  .tile-label{position:absolute;top:590px;width:280px;display:flex;justify-content:space-between;align-items:center;font-family:"Michroma",sans-serif;font-size:17px;text-transform:uppercase;padding:0 4px}
  .ghost-surf{font-size:64px;color:var(--ghost);transform:rotate(-90deg);width:440px;text-align:center;left:-166px;top:418px}

  /* footer */
  .site-footer{position:absolute;left:0;top:2739px;width:1200px;height:385px;background:var(--blue)}
  .footer-brand{position:absolute;width:100%;top:75px;text-align:center;font-family:"Michroma",sans-serif;font-size:64px}
  .footer-contact{position:absolute;top:202px;width:100%;display:flex;justify-content:center;align-items:center;gap:34px;font-size:15px}
  .footer-contact span{display:flex;align-items:center;gap:8px}
  .social{position:absolute;top:258px;width:100%;display:flex;justify-content:center;gap:17px}
  .social span{width:43px;height:43px;border:2px solid var(--white);border-radius:50%;display:flex;align-items:center;justify-content:center}
  .social span i{width:14px;height:14px;border-radius:50%;background:var(--red)}
  .copyright{position:absolute;top:333px;width:100%;text-align:center;font-size:15px}
</style>
</head>
<body>

<header class="site-header">
  <div class="brand">BSRA</div>
  <nav class="nav"><span>HOME</span><span>ABOUT</span><span>WHY LASER</span><span>CAPABILITIES</span></nav>
  <div class="btn btn-red btn-contact">Contact</div>
</header>

<section class="hero" role="img" aria-label="Welder in protective mask grinding metal with sparks flying, over a red Australian flag backdrop">
  <div class="abs display hero-welcome">Welcome to</div>
  <div class="abs display hero-name">BSRA</div>
  <div class="abs hero-sub">Brightwave Surface Renewal Australia</div>
  <div class="btn btn-blue btn-start">Get Started</div>
</section>

<section class="why">
  <h2 class="display why-title">Why choose laser</h2>
  <div class="why-item" style="left:58px">Minimum downtime</div>
  <div class="why-active" role="img" aria-label="Explainer video thumbnail">No surface damage
    <svg width="16" height="16" viewBox="0 0 16 16" style="display:block;margin:6px auto 0"><path d="M3 1 L14 8 L3 15 Z" fill="#fff"/></svg>
  </div>
  <div class="why-item" style="left:476px">No environmental impact</div>
  <div class="why-item" style="left:724px">No mess</div>
  <div class="why-item" style="left:854px">No waste</div>
  <div class="why-item" style="left:990px">Complete restoration</div>
</section>

<section class="about">
  <div class="abs display ghost-about">About</div>
  <div class="abs frame-red"></div>
  <div class="abs frame-white"></div>
  <div class="abs about-photo" role="img" aria-label="Two welders in helmets working with bright sparks"></div>
  <div class="abs display about-label">About</div>
  <h2 class="abs display about-heading">Brightwave <span class="red">Surface</span><br><span class="red">Renewal</span> Australia</h2>
  <p class="abs about-text">Background Information - Brightwave Surface Renewal Australia (BSRA) is a leading provider of advanced laser restoration services for the residential, commercial, medical, hazardous and industrial sectors, offering waste free, chemical free and damage free complete restoration of metals, concrete, wood, stone and heritage, hygiene and hazard surfaces, with complete removal of coatings, bacteria, paint, rust, graffiti, mold and fire ash (soot), and preparation and treating for welding and bonding.</p>
  <div class="btn btn-blue btn-learn">Learn More</div>
</section>

<section class="contaminants">
  <div class="abs display ghost-cont">Contaminants</div>
  <h2 class="display cont-title">We clean <span class="red">contaminants like</span></h2>
  <div class="cards">
    <div class="card"><div class="card-icon" role="img" aria-label="Bacteria icon"><svg width="44" height="44"><circle cx="22" cy="22" r="16" fill="none" stroke="#fff" stroke-width="2"/></svg></div>Bacteria</div>
    <div class="card"><div class="card-icon" role="img" aria-label="Rust icon"><svg width="44" height="44"><circle cx="22" cy="22" r="16" fill="none" stroke="#fff" stroke-width="2"/></svg></div>Rust</div>
    <div class="card"><div class="card-icon" role="img" aria-label="Corrosion icon"><svg width="44" height="44"><circle cx="22" cy="22" r="16" fill="none" stroke="#fff" stroke-width="2"/></svg></div>Corrosion</div>
    <div class="card"><div class="card-icon" role="img" aria-label="Oil icon"><svg width="44" height="44"><circle cx="22" cy="22" r="16" fill="none" stroke="#fff" stroke-width="2"/></svg></div>Oil</div>
    <div class="card"><div class="card-icon" role="img" aria-label="Oxides icon"><svg width="44" height="44"><circle cx="22" cy="22" r="16" fill="none" stroke="#fff" stroke-width="2"/></svg></div>Oxides</div>
    <div class="card"><div class="card-icon" role="img" aria-label="Grease icon"><svg width="44" height="44"><circle cx="22" cy="22" r="16" fill="none" stroke="#fff" stroke-width="2"/></svg></div>Grease</div>
    <div class="card"><div class="card-icon" role="img" aria-label="Paint icon"><svg width="44" height="44"><circle cx="22" cy="22" r="16" fill="none" stroke="#fff" stroke-width="2"/></svg></div>Paint</div>
    <div class="card"><div class="card-icon" role="img" aria-label="Mold icon"><svg width="44" height="44"><circle cx="22" cy="22" r="16" fill="none" stroke="#fff" stroke-width="2"/></svg></div>Mold</div>
  </div>
  <div class="btn btn-blue btn-viewall-cont">View All</div>
</section>

<section class="surfaces">
  <div class="abs display ghost-surf">Surfaces</div>
  <div class="btn btn-red tab-surfaces">Surfaces</div>
  <div class="btn btn-outline tab-industries">Industries</div>
  <h2 class="abs display surf-heading">Surfaces</h2>
  <div class="btn btn-red btn-viewall-surf">View All</div>

  <div class="tile" style="left:113px;background:linear-gradient(160deg,#6b6b6b,#c9822e 55%,#3a2a1c)" role="img" aria-label="Metal being cut with sparks"></div>
  <div class="tile" style="left:461px;background:linear-gradient(160deg,#ff2a30,#e0121a 60%,#c80f16)" role="img" aria-label="Engine parts in red tint"></div>
  <div class="tile" style="left:808px;background:linear-gradient(160deg,#3c3c3c,#5a5a5a 50%,#2c2c2c)" role="img" aria-label="Assorted hand tools laid out"></div>

  <div class="tile-label" style="left:113px"><span>Metals</span><svg width="20" height="12"><path d="M0 6H17M12 1L18 6L12 11" stroke="#fff" stroke-width="1.6" fill="none"/></svg></div>
  <div class="tile-label" style="left:461px"><span>Engines</span><svg width="20" height="12"><path d="M0 6H17M12 1L18 6L12 11" stroke="#fff" stroke-width="1.6" fill="none"/></svg></div>
  <div class="tile-label" style="left:808px"><span>Tools</span><svg width="20" height="12"><path d="M0 6H17M12 1L18 6L12 11" stroke="#fff" stroke-width="1.6" fill="none"/></svg></div>
</section>

<footer class="site-footer">
  <div class="footer-brand">BSRA</div>
  <div class="footer-contact">
    <span><svg width="12" height="16" viewBox="0 0 12 16"><path d="M6 0C2.7 0 0 2.6 0 5.9 0 10 6 16 6 16s6-6 6-10.1C12 2.6 9.3 0 6 0zm0 8.2a2.3 2.3 0 1 1 0-4.6 2.3 2.3 0 0 1 0 4.6z" fill="#fff"/></svg>Perth | Darwin</span>
    <span>|</span>
    <span><svg width="15" height="15" viewBox="0 0 16 16"><path d="M3.6 1l2.4 3-1.5 1.8c.9 2 2.5 3.6 4.6 4.6L10.9 9 14 11.4 12.8 14C7 14 2 9 2 3.2z" fill="#fff"/></svg>+61 (3) 5550 0142</span>
    <span>|</span>
    <span><svg width="16" height="12" viewBox="0 0 16 12"><rect width="16" height="12" rx="1" fill="#fff"/><path d="M1 1l7 6 7-6" stroke="#1a73c0" stroke-width="1.4" fill="none"/></svg>&nbsp;&nbsp;hello@brightwave-sr.com.au</span>
  </div>
  <div class="social"><span><i></i></span><span><i></i></span><span><i></i></span></div>
  <div class="copyright">©Copyrights 2023 BSRA &nbsp;|&nbsp;&nbsp; All Rights Reserved</div>
</footer>

</body>
</html>
```